Velmora Outcomes Brochure Design Project

- Who we are?
Velmora Outcomes is New Internet Marketing Company Based in China.

It is our aim to provide Chinese clients with the means to internationally market their product, via the Internet.

Our primary products are Outsourced Design ( Thanks to Pixel hive and the amazing designers who use it), SEO and Virtual Hosting.

- Project Brief
Design a vibrant and fresh brochure that introduces the fundamentals of SEO. There is no restriction to the number of pages, however all the info I have included in this brief must be included.

- Colour Palette
Please see link or download the Adobe Swatch Exchange File or follow the link below
http://tintaro.example.com/#themes/search?term=5830716
Updates

Logo updated - grey background removed

Various file formats added for logo and brochure content

Brochure zip file add containing logo in different formats.

Adobe color scheme file added

The general corporate colors are:

Base Color: CMYK :0, 60, 80, 0  Hex: FF6633
Dark Orange: CMYK: 0, 72, 96, 30 Hex: B23308
Light Orange: CMYK 0, 42, 56, 0 Hex: FF9571
Grey: CMYK 0, 0, 0, 48 Hex: 858585
Light Grey: CMYK 0, 0, 0, 26 Hex: BDBDBD

Please note that I'm happy for other colors to be included, however I would like these the corporate branding colors to be clearly present through the brochure.

Hi All

First place payment has increased to $600 - Looking to see some creative designs!

Hi All

Project Deadline Extended
Reason: I have increase the budget and extend the deadline as I need to see more design.

I have attached a zip file that contains example brochures I like.

We are not keen on the table data its a little plain. We have create an info-graphic to replace one of the table and would like to see it included in the design.

Project Deadline Extended
Reason: A few designers have asked for this extension and I would like to see additional designs. Thanks Marek

Target Market(s)

- Our Target Audience is..
It is small to medium businesses looking to reach out to the international market.
Our clients still very much operate on a face to face level in business and are new to the concept of Internet marketing

However this must look professional, Marketable and Clean, with the power of connecting people globally, through SEO and design to be reflected visually in the brochure.

Industry/Entity Type

Internet

Requirements
Must have
• One or more of the FACTS that I have highlighted need to stand out on each page. These FACTS can be found the document attached to this brief and are under the section titled 'Did You Know!'. Not every fact in this section needs to be highlighted in the brochure, but each page needs to have at least, one or more fact that stands out, soemwhere on the page.
See attached document, under the heading 'Did you Know!' and use one or two of these facts to spruce up the pages!

One image/ per page or per two pages MUST be included!

- Provide stock photos and please send us a message with the additional cost of these with your submission

The Table data, that I have included in the attachment must be included in the body of the pages - BUT the table format is not necessary and you can place the information in the body like plain text.

The brochure size should be a little larger than A4.

Please design the back page, like a pocket to hold paper and other material in it that I include with this brochure.

```html
<!DOCTYPE html>
<html lang="en">
<head>
<meta charset="utf-8">
<title>Velmora Outcomes – SEO Brochure</title>
<link href="https://fonts.googleapis.com/css2?family=Open+Sans:wght@400;600;700&display=swap" rel="stylesheet">
<style>
:root{
  --orange:#FF6633;
  --orange-dark:#B23308;
  --orange-light:#FF9571;
  --grey:#858585;
  --grey-light:#BDBDBD;
  --grey-pale:#e6e6e6;
  --navy:#0d2c46;
  --navy-mid:#275a82;
  --ink:#444;
  --paper:#ffffff;
}
*{box-sizing:border-box;margin:0;padding:0}
html,body{width:748px;height:1200px;overflow:hidden;background:var(--paper)}
body{position:relative;font-family:"Open Sans",Arial,sans-serif;color:var(--ink);font-size:5.4px;line-height:1.4}
.band{position:absolute;left:110px;width:570px;background:linear-gradient(90deg,var(--navy) 0%,var(--navy-mid) 60%,#5d8fb6 100%)}
.band--front{top:0;height:220px}
.band--back{top:1058px;height:142px;background:linear-gradient(90deg,var(--navy-mid) 0%,var(--navy) 45%,#5d8fb6 100%)}
.cover{position:absolute;left:402px;top:0;width:126px;height:212px;background:linear-gradient(160deg,#9fc6e6 0%,#3f79a8 45%,#13365a 100%);box-shadow:0 2px 6px rgba(0,0,0,.35)}
.cover__brand{position:absolute;left:14px;bottom:16px;color:#fff;font-weight:700;font-size:8px;display:flex;align-items:center;gap:4px}
.cover__brand i{width:7px;height:7px;background:var(--orange);display:block}
.backcover{position:absolute;left:47px;top:0;width:126px;height:142px;background:linear-gradient(150deg,#d8e6f2 0%,#7fa6c8 40%,#1f4a72 100%)}
.page{position:absolute;width:280px;background:var(--paper);box-shadow:0 0 0 .5px #ddd;overflow:hidden}
.page--left{left:110px}
.page--right{left:392px}
.photo{position:absolute}
.photo-title{position:absolute;color:#fff;font-weight:700;font-size:15px;line-height:1.05}
.col{position:absolute}
.h{font-weight:700;color:var(--orange);font-size:6.6px;margin:5px 0 2px}
.h--dark{color:var(--ink)}
p{margin-bottom:3px}
ul{list-style:none}
li{padding-left:6px;position:relative}
li:before{content:"";position:absolute;left:0;top:2.5px;width:3px;height:3px;background:var(--orange)}
.fact{position:absolute;background:var(--orange);color:#fff;font-weight:600;font-size:6px;padding:5px 8px}
.fact--box{padding:6px}
table{width:100%;border-collapse:collapse;font-size:5.2px;margin-bottom:4px}
th{background:var(--orange);color:#fff;text-align:left;padding:2px 3px;font-weight:600}
td{padding:2px 3px;background:var(--grey-pale)}
tr:nth-child(odd) td{background:#f4f4f4}
td:first-child{color:var(--grey);font-weight:600}
.chart{position:absolute;left:40px;top:8px}
.chart text{font-size:6px;fill:var(--grey);font-family:"Open Sans",Arial,sans-serif}
</style>
</head>
<body>

<div class="band band--front">
  <div class="cover" role="img" aria-label="Cover photo: businessman touching a glowing network screen">
    <div class="cover__brand"><i></i>Velmora Outcomes</div>
  </div>
</div>

<!-- Spread 1 -->
<section class="page page--left" style="top:212px;height:196px">
  <div class="photo" style="left:0;top:0;width:105px;height:160px;background:linear-gradient(160deg,#d7dfe6,#7d93a8 60%,#3b5570)" role="img" aria-label="Photo: businessman pointing at search icons"></div>
  <div class="photo-title" style="left:10px;top:18px">SEO</div>
  <div class="col" style="left:112px;top:8px;width:160px">
    <p>Search engine optimisation helps your business appear when global buyers search online for the products you make.</p>
    <div class="h">Why it matters</div>
    <p>Most buyers now begin with a search. Ranking well builds trust and brings steady traffic.</p>
    <ul><li>Keyword research</li><li>On-page content</li><li>Quality links</li><li>Monthly reports</li></ul>
  </div>
  <div class="fact" style="left:0;top:166px;width:280px">Did you know? Most users never scroll past the first page of results.</div>
</section>
<section class="page page--right" style="top:212px;height:196px">
  <div class="col" style="left:8px;top:6px;width:126px">
    <div class="h h--dark">The Basics of SEO</div>
    <table><tr><th>Factor</th><th>Impact</th></tr><tr><td>Keywords</td><td>High</td></tr><tr><td>Content</td><td>High</td></tr><tr><td>Links</td><td>Medium</td></tr><tr><td>Speed</td><td>Medium</td></tr></table>
  </div>
  <div class="col" style="left:146px;top:22px;width:126px">
    <table><tr><th>Service</th><th>Detail</th></tr><tr><td>Audit</td><td>Full site</td></tr><tr><td>Setup</td><td>One week</td></tr><tr><td>Reports</td><td>Monthly</td></tr></table>
  </div>
  <div class="fact" style="left:0;top:166px;width:280px">Did you know? Search drives more site visits than social media.</div>
</section>

<!-- Spread 2 -->
<section class="page page--left" style="top:412px;height:196px">
  <div class="photo" style="left:0;top:0;width:105px;height:196px;background:linear-gradient(180deg,#eef0f2,#a9b1b9 55%,#6c7680)" role="img" aria-label="Photo: glass office building"></div>
  <div class="photo-title" style="left:8px;top:40px;font-size:13px">SEO Packages</div>
  <div class="col" style="left:112px;top:8px;width:160px">
    <div class="h">Starter Package</div>
    <p>A simple plan for small firms taking first steps online.</p>
    <table><tr><td>Keywords</td><td>10</td></tr><tr><td>Pages</td><td>5</td></tr><tr><td>Reports</td><td>Monthly</td></tr></table>
    <div class="h">Business Package</div>
    <table><tr><td>Keywords</td><td>25</td></tr><tr><td>Pages</td><td>15</td></tr></table>
  </div>
</section>
<section class="page page--right" style="top:412px;height:196px">
  <div class="col" style="left:8px;top:4px;width:126px">
    <div class="h">Premium Package</div>
    <p>For growing brands ready to reach buyers abroad.</p>
    <table><tr><td>Keywords</td><td>50</td></tr><tr><td>Pages</td><td>30</td></tr><tr><td>Links</td><td>100</td></tr></table>
    <div class="h">Enterprise Package</div>
    <table><tr><td>Keywords</td><td>100</td></tr><tr><td>Pages</td><td>60</td></tr></table>
  </div>
  <div class="col" style="left:146px;top:4px;width:126px">
    <div class="h">Hosting Options</div>
    <table><tr><td>Storage</td><td>20 GB</td></tr><tr><td>Domains</td><td>5</td></tr><tr><td>Email</td><td>Included</td></tr></table>
    <div class="h">Support Plans</div>
    <table><tr><td>Hours</td><td>24/7</td></tr><tr><td>Response</td><td>1 day</td></tr></table>
  </div>
  <div class="fact" style="left:0;top:170px;width:280px">Did you know? Nearly half of searches have local intent.</div>
</section>

<!-- Spread 3 -->
<section class="page page--left" style="top:612px;height:208px">
  <div class="col" style="left:10px;top:6px;width:260px">
    <div class="h">How Search Works</div>
    <p>Engines crawl pages, store them in an index, then rank results by relevance and trust.</p>
  </div>
  <div class="fact fact--box" style="left:10px;top:40px;width:130px">Did you know? Billions of searches are made every day.</div>
  <div class="col" style="left:10px;top:62px;width:130px">
    <div class="h">Going Global</div>
    <p>We translate and tune your site for each target market.</p>
  </div>
  <div class="photo" style="left:90px;top:98px;width:190px;height:110px;background:radial-gradient(circle at 45% 55%,#dfeefa 0%,#7fb2dc 35%,#2f6fa6 70%,#dbe8f3 100%)" role="img" aria-label="Illustration: glowing globe with network lines"></div>
</section>
<section class="page page--right" style="top:612px;height:208px">
  <div class="col" style="left:8px;top:6px;width:140px">
    <div class="h">Virtual Hosting</div>
    <p>Fast, secure servers keep your site online and quick to load for visitors everywhere.</p>
    <p>We manage updates, backups and security so you can focus on sales.</p>
  </div>
  <div class="fact fact--box" style="left:8px;top:130px;width:140px">Did you know? Slow pages lose nearly half of visitors.</div>
  <div class="photo" style="left:155px;top:0;width:125px;height:208px;background:linear-gradient(160deg,#f2b08a 0%,#e0703a 35%,#2c4f6e 80%)" role="img" aria-label="Photo: hand touching a network of connected people icons"></div>
</section>

<!-- Spread 4 -->
<section class="page page--left" style="top:824px;height:198px">
  <div class="photo" style="left:0;top:0;width:105px;height:198px;background:linear-gradient(170deg,#f1f1f1,#b9bcc0 55%,#6f747a)" role="img" aria-label="Photo: businesswoman writing at a desk"></div>
  <div class="photo-title" style="left:8px;top:36px;font-size:12px">Logo and<br>Website Design</div>
  <div class="col" style="left:112px;top:8px;width:160px">
    <p>A strong brand and a clear website win trust before the first meeting.</p>
    <div class="h">Design Services</div>
    <ul><li>Logo design</li><li>Brand guides</li><li>Website layout</li><li>Print material</li></ul>
  </div>
  <div class="fact fact--box" style="left:112px;top:150px;width:160px">Did you know? Visitors judge a website in under a second.</div>
</section>
<section class="page page--right" style="top:824px;height:198px">
  <div class="col" style="left:8px;top:4px;width:140px"><div class="h h--dark">How We Work Together</div></div>
  <svg class="chart" width="200" height="190" viewBox="-100 -95 200 190">
    <circle r="82" fill="none" stroke="var(--grey-light)" stroke-width=".6"/>
    <circle r="60" fill="none" stroke="var(--grey-light)" stroke-width=".6"/>
    <g fill="var(--orange)" stroke="#fff" stroke-width="1.5">
      <path d="M0 0L0 -70A70 70 0 0 1 49.5 -49.5Z"/>
      <path transform="rotate(45)" fill="var(--orange-light)" d="M0 0L0 -55A55 55 0 0 1 38.9 -38.9Z"/>
      <path transform="rotate(90)" fill="var(--orange-dark)" d="M0 0L0 -80A80 80 0 0 1 56.6 -56.6Z"/>
      <path transform="rotate(135)" d="M0 0L0 -45A45 45 0 0 1 31.8 -31.8Z"/>
      <path transform="rotate(180)" fill="var(--orange-light)" d="M0 0L0 -65A65 65 0 0 1 46 -46Z"/>
      <path transform="rotate(225)" d="M0 0L0 -50A50 50 0 0 1 35.4 -35.4Z"/>
      <path transform="rotate(270)" fill="var(--orange-dark)" d="M0 0L0 -75A75 75 0 0 1 53 -53Z"/>
      <path transform="rotate(315)" fill="var(--orange-light)" d="M0 0L0 -60A60 60 0 0 1 42.4 -42.4Z"/>
    </g>
    <circle r="16" fill="#fff"/>
    <g text-anchor="middle">
      <text x="34.4" y="-83.2">Research</text>
      <text x="83.2" y="-34.4">Strategy</text>
      <text x="83.2" y="36.4">Content</text>
      <text x="34.4" y="88">Links</text>
      <text x="-34.4" y="88">Tracking</text>
      <text x="-83.2" y="36.4">Reporting</text>
      <text x="-83.2" y="-34.4">Review</text>
      <text x="-34.4" y="-83.2">Growth</text>
    </g>
  </svg>
</section>

<div class="band band--back">
  <div class="backcover" role="img" aria-label="Back cover: pale blue hexagon pattern"></div>
</div>

</body>
</html>
```